SKYVANTEX (drone photo and video) and Photogrammetry Services (mapping and 3D modeling)

We need a business card design for a SKYVANTEX. Our businesses provides (drone) Aerial Photo and Video Captures. However we also provide Photogrammetry (which is 3D modeling and mapping). We greatly value unique points of view taken of landscapes and subjects with aerial photography and videography. 3D modeling and mapping is the other area of focus and have an incredibly broad scope of applications and imaginative creativity.

Target Market(s)

Based out of Northern Virginia and serving the greater Virginia and Maryland areas

Industry/Entity Type

Drone Photo and video and Photogrammetry Services (mapping and 3D modeling)

Contact Information for Business Card

3D Models, Maps and Photo/Video Production name: Marcus Pettibone email: mqp@skyvantex.us website: skyvantex.us phone: 571-806-3394; please also include "Aerial Photo/Video and 3D Mapping/Modeling"

Requirements
Must have
• Please make this design vertical and double sided. The selection box is not letting me choose Double Sided but that is my wish. Incorporate uploaded LOGO and color scheme
Nice to have
• Preferably does not feel too crowded and balances not having an exaggerated amount of distracting detail
Should not have
• do not cram bullet points or text in long form

```html
<!DOCTYPE html>
<html lang="en">
<head>
<meta charset="utf-8">
<title>SKYVANTEX Business Card</title>
<link href="https://fonts.googleapis.com/css2?family=Jost:wght@400;500;600&display=swap" rel="stylesheet">
<style>
  :root {
    --stage: #1f1f1f;
    --amber: #f9a62a;
    --orange: #f37a2c;
    --red: #ee2d2e;
    --white: #ffffff;
    --ink: #141414;
    --ink-soft: #4a4a4a;
  }
  * { margin: 0; padding: 0; box-sizing: border-box; }
  html, body {
    width: 1200px;
    height: 1200px;
    overflow: hidden;
    background: var(--stage);
    font-family: "Jost", sans-serif;
  }
  .stage { position: relative; width: 1200px; height: 1200px; }
  .card {
    position: absolute;
    top: 303px;
    height: 594px;
    overflow: hidden;
    box-shadow: 3px 3px 6px rgba(0,0,0,0.55);
  }

  /* Front */
  .card-front {
    left: 200px;
    width: 369px;
    background: linear-gradient(135deg, var(--amber) 0%, var(--orange) 45%, var(--orange) 70%, #f1582d 100%);
  }
  .card-front .facets { position: absolute; inset: 0; width: 100%; height: 100%; }
  .card-front .drone-decor {
    position: absolute;
    left: 0;
    top: 85px;
    width: 212px;
    height: 233px;
    background: linear-gradient(135deg, rgba(249,166,42,0.45), rgba(243,122,44,0));
    border-radius: 0 8px 60px 0;
  }
  .card-front .wordmark {
    position: absolute;
    left: 0; right: 0;
    top: 478px;
    text-align: center;
    color: var(--white);
    font-weight: 600;
    font-size: 46px;
    letter-spacing: 0.5px;
    line-height: 1;
  }
  .card-front .tagline {
    position: absolute;
    left: 0; right: 0;
    top: 532px;
    text-align: center;
    color: var(--white);
    font-weight: 500;
    font-size: 13px;
    letter-spacing: 0.6px;
    line-height: 1;
  }

  /* Back */
  .card-back { left: 599px; width: 364px; background: var(--white); }
  .card-back .lower-band {
    position: absolute;
    left: 0; right: 0;
    top: 330px; bottom: 0;
    background: linear-gradient(180deg, var(--amber) 0%, var(--orange) 50%, var(--red) 100%);
  }
  .card-back .logo-dot {
    position: absolute;
    left: 107px;
    top: 61px;
    width: 150px;
    height: 112px;
    border-radius: 75px 75px 0 0;
    background: var(--orange);
  }
  .card-back .wordmark {
    position: absolute;
    left: 0; right: 0;
    top: 180px;
    text-align: center;
    color: var(--ink);
    font-weight: 600;
    font-size: 46px;
    letter-spacing: 0.5px;
    line-height: 1;
  }
  .card-back .person {
    position: absolute;
    left: 0; right: 0;
    top: 238px;
    text-align: center;
    color: var(--ink-soft);
    font-weight: 500;
    font-size: 16px;
    letter-spacing: 1px;
    line-height: 1;
  }
  .card-back .drone-visual {
    position: absolute;
    left: 44px;
    right: 44px;
    top: 296px;
    height: 143px;
    border-radius: 48px 48px 24px 24px;
    background: linear-gradient(180deg, rgba(20,20,20,0.12), rgba(20,20,20,0.18));
  }
  .card-back .contact {
    position: absolute;
    left: 0; right: 0;
    top: 454px;
    text-align: center;
    color: var(--white);
    font-weight: 500;
    list-style: none;
  }
  .contact .phone { font-size: 26px; line-height: 30px; margin-bottom: 6px; }
  .contact .email,
  .contact .web { font-size: 23px; line-height: 28px; margin-bottom: 8px; }
</style>
</head>
<body>
<main class="stage">

  <section class="card card-front" aria-label="Card front">
    <svg class="facets" viewBox="0 0 369 594" preserveAspectRatio="none" aria-hidden="true">
      <defs>
        <linearGradient id="bandRed" x1="0" y1="1" x2="1" y2="0">
          <stop offset="0" stop-color="#ee2d2e"/>
          <stop offset="1" stop-color="#f37a2c"/>
        </linearGradient>
        <linearGradient id="bandLight" x1="0" y1="1" x2="1" y2="0">
          <stop offset="0" stop-color="#f1582d"/>
          <stop offset="1" stop-color="#f37a2c"/>
        </linearGradient>
      </defs>
      <polygon points="369,163 369,594 0,594 0,535" fill="url(#bandRed)"/>
      <polygon points="336,296 20,594 369,594 369,526 238,540" fill="url(#bandLight)"/>
    </svg>
    <div class="drone-decor" role="img" aria-label="Faint close-up of a drone arm and propeller"></div>
    <h1 class="wordmark">SKYVANTEX</h1>
    <p class="tagline">AERIAL PHOTO/VIDEO AND 3D MAPPING/MODELING</p>
  </section>

  <section class="card card-back" aria-label="Card back">
    <div class="lower-band"></div>
    <div class="logo-dot" aria-hidden="true"></div>
    <h2 class="wordmark">SKYVANTEX</h2>
    <p class="person">MARCUS PETTIBONE</p>
    <div class="drone-visual" role="img" aria-label="Black silhouette of a quadcopter drone with landing legs"></div>
    <ul class="contact">
      <li class="phone">571-806-3394</li>
      <li class="email">MQP@SKYVANTEX.US</li>
      <li class="web">SKYVANTEX.US</li>
    </ul>
  </section>

</main>
</body>
</html>
```